Business card design for upmarket Home Technology design and Installation company

Hello designers, we need a great business card designed.
We need it to convey high tech, and also sophistication .
We work with some of the most affluent people in the world building them home technology systems, and A/V entertainment systems.

Services offered include the following:
Design, sales, installation, and maintenance of

*Home Automation systems
*Distributed / Multi-Room Audio and Video
*High Performance Networks & WiFi
* Lighting and Shade Control
*Home cinema
*Security and CCTV Systems

I have included a copy of our logo to use for your design efforts.

Target Market(s)

Upmarket clients with multi million euro villas.

Industry/Entity Type

Home technology

Contact Information for Business Card

NAME: Derek Halloran ADDRESS: Plaza Brisa Local 42, Port Andratx, 07392 PHONE: +34-602-518-794 EMAIL: DHalloran@VELTRAsmarthomes.com WEB: www.veltrasmarthomes.com

Requirements
Must have
• Our Logo, and our tagline

```html
<!DOCTYPE html>
<html lang="en">
<head>
<meta charset="utf-8">
<title>VELTRA Smart Homes – Business Card</title>
<link href="https://fonts.googleapis.com/css2?family=Poppins:wght@500;600&family=Source+Sans+3:wght@400;600;700&display=swap" rel="stylesheet">
<style>
  :root {
    --backdrop: #5b5b5b;
    --card-white: #ffffff;
    --card-black: #121212;
    --gold: #c6a25c;
    --gold-deep: #b8914a;
    --gold-light: #f6dc9f;
    --gold-text: #e9c67a;
    --ink: #1a1a1a;
    --rule: #9a9a9a;
    --service-text: #e4e4e4;
  }
  * { margin: 0; padding: 0; box-sizing: border-box; }
  html, body { width: 1093px; height: 1200px; overflow: hidden; }
  body {
    background: var(--backdrop);
    position: relative;
    font-family: "Source Sans 3", sans-serif;
  }
  .card {
    position: absolute;
    left: 265px;
    width: 577px;
    height: 356px;
    border-radius: 33px;
    overflow: hidden;
    box-shadow: 3px 4px 6px rgba(0,0,0,0.55);
  }
  .card--front { top: 226px; background: var(--card-white); }
  .card--back { top: 621px; background: var(--card-black); }

  /* Front: brand block */
  .brand-mark {
    position: absolute;
    left: 107px; top: 97px;
    width: 100px; height: 100px;
    border-radius: 50%;
    background: var(--gold);
  }
  .brand-name {
    position: absolute;
    left: 60px; top: 226px;
    width: 194px;
    text-align: center;
    font-family: "Poppins", sans-serif;
    font-weight: 500;
    font-size: 33px;
    letter-spacing: 0.16em;
    color: var(--gold);
    line-height: 1;
  }
  .divider {
    position: absolute;
    left: 261px; top: 102px;
    width: 1.5px; height: 151px;
    background: var(--rule);
  }

  /* Front: contact block */
  .holder-name {
    position: absolute;
    left: 285px; top: 96px;
    font-family: "Poppins", sans-serif;
    font-weight: 600;
    font-size: 24px;
    color: var(--gold);
    line-height: 1.2;
  }
  .contact-list {
    position: absolute;
    left: 285px; top: 138px;
    list-style: none;
  }
  .contact-list li {
    display: flex;
    align-items: center;
    height: 21px;
    font-size: 17px;
    color: var(--ink);
  }
  .contact-list svg { width: 15px; height: 15px; margin-right: 7px; flex: none; }
  .address {
    position: absolute;
    left: 285px; top: 212px;
    font-size: 17px;
    line-height: 21px;
    color: var(--ink);
    font-style: normal;
  }

  /* Front: bottom band */
  .band-stripe {
    position: absolute;
    left: 0; top: 308px;
    width: 100%; height: 6px;
    background: var(--gold-light);
  }
  .band {
    position: absolute;
    left: 0; top: 318px;
    width: 100%; height: 38px;
    background: var(--gold);
  }
  .band-disc {
    position: absolute;
    left: 460px; top: 285px;
    width: 71px; height: 71px;
    border-radius: 50%;
    background: var(--card-white);
  }

  /* Back */
  .back-name {
    position: absolute;
    left: 0; top: 104px;
    width: 100%;
    text-align: center;
    font-family: "Poppins", sans-serif;
    font-weight: 500;
    font-size: 78px;
    letter-spacing: 0.2em;
    padding-left: 0.2em;
    color: var(--gold);
    line-height: 1;
  }
  .tagline {
    position: absolute;
    left: 39px; top: 238px;
    font-weight: 700;
    font-size: 15.5px;
    letter-spacing: -0.01em;
    color: var(--gold-text);
    text-transform: uppercase;
  }
  .services {
    position: absolute;
    top: 270px;
    list-style: none;
  }
  .services--left { left: 39px; }
  .services--right { left: 358px; }
  .services li {
    position: relative;
    padding-left: 13px;
    height: 18.5px;
    line-height: 18.5px;
    font-size: 15.5px;
    color: var(--service-text);
  }
  .services li::before {
    content: "";
    position: absolute;
    left: 0; top: 6px;
    width: 7px; height: 7px;
    border-radius: 50%;
    background: var(--gold);
  }
</style>
</head>
<body>

<section class="card card--front" aria-label="Business card front">
  <div class="brand-mark"></div>
  <div class="brand-name">VELTRA</div>
  <div class="divider"></div>

  <h1 class="holder-name">Derek Halloran</h1>
  <ul class="contact-list">
    <li>
      <svg viewBox="0 0 16 16" aria-hidden="true"><path d="M3.2 1.5l2.3 2.6-1.2 1.6c.9 2 2.5 3.6 4.5 4.6l1.6-1.2 2.6 2.3-1.4 2.1C6.4 13.4 2.6 9.6 1.1 4.4z" fill="none" stroke="var(--gold)" stroke-width="1.4" stroke-linejoin="round"/><path d="M9.5 2.5a4 4 0 014 4M9.5 5a1.6 1.6 0 011.6 1.6" fill="none" stroke="var(--gold)" stroke-width="1.2" stroke-linecap="round"/></svg>
      +34-602-518-794
    </li>
    <li>
      <svg viewBox="0 0 16 16" aria-hidden="true"><rect x="0.5" y="3" width="15" height="10" fill="var(--gold)"/><path d="M0.5 3l7.5 6 7.5-6" fill="none" stroke="#fff" stroke-width="1.2"/></svg>
      DHalloran@VELTRAsmarthomes.com
    </li>
    <li>
      <svg viewBox="0 0 16 16" aria-hidden="true"><g fill="none" stroke="var(--gold)" stroke-width="1.1"><circle cx="8" cy="8" r="6.5"/><ellipse cx="8" cy="8" rx="2.8" ry="6.5"/><path d="M1.5 8h13M2.5 4.8h11M2.5 11.2h11"/></g></svg>
      www.veltrasmarthomes.com
    </li>
  </ul>
  <address class="address">
    Plaza Brisa Local 42<br>
    Port Andratx, 07392
  </address>

  <div class="band-stripe"></div>
  <div class="band"></div>
  <div class="band-disc"></div>
</section>

<section class="card card--back" aria-label="Business card back">
  <div class="back-name">VELTRA</div>
  <h2 class="tagline">Design, sales, installation, and maintenance of</h2>
  <ul class="services services--left">
    <li>Home Automation systems</li>
    <li>Distributed / Multi-Room Audio and Video</li>
    <li>High Performance Networks &amp; WiFi</li>
  </ul>
  <ul class="services services--right">
    <li>Lighting and Shade Control</li>
    <li>Home cinema</li>
    <li>Security and CCTV Systems</li>
  </ul>
</section>

</body>
</html>
```